STOREFRONT LIT SIGN for The Ranchera Loft

A sign advertising our music academy. This sign will be hung 10 feet above the entrance of our building and will be seen by all pedestrian and vehicle traffic on Birch Lane Delano.

Target Market(s)

Street passerby

Industry/Entity Type

Music Training

Font styles to use
Other font styles liked:
• Creative

Colors

Designer to choose colors to be used in the design.

Requirements
Must have
• A White Background
• Dimensions: 8 ft long x 3 ft tall
• The Ranchera Loft of Delano
• Lecciones de Piano, Violin, Guitarra, Voz, Trompeta y Mas
• MUSIC ACADEMY *(This should be most prominent)
• Guitar, Voice, Trumpet and More
• (661) 555-0147
• therancheraloft.example
Nice to have
• Graphics of a piano, or guitar, or violin or trumpet or a combination of two or more

```html
<!DOCTYPE html>
<html lang="en">
<head>
<meta charset="utf-8">
<title>The Ranchera Loft of Delano – Storefront Sign</title>
<link rel="stylesheet" href="https://fonts.googleapis.com/css2?family=Montserrat:wght@600;700;800;900&display=swap">
<style>
  :root {
    --stage: #4a4a4a;
    --band-blue: #1b3a8c;
    --headline-red: #d50d12;
    --ink: #111111;
    --ink-soft: #3a3a3a;
    --sign-white: #ffffff;
    --sign-mist: #e6e9ec;
    --caption: #f2f2f2;
  }
  * { box-sizing: border-box; margin: 0; padding: 0; }
  html, body { width: 1200px; height: 581px; overflow: hidden; }
  body {
    background: var(--stage);
    font-family: "Montserrat", Arial, sans-serif;
    position: relative;
  }
  .sign {
    position: absolute;
    left: 74px; top: 74px;
    width: 1056px; height: 396px;
    background: linear-gradient(170deg, var(--sign-mist) 0%, #f4f5f7 35%, var(--sign-white) 70%, #eef0f2 100%);
    box-shadow: 0 10px 24px rgba(0,0,0,.35);
    overflow: hidden;
  }
  .sign__band {
    height: 54px;
    background: var(--band-blue);
    display: flex; align-items: center; justify-content: center;
  }
  .sign__band-title {
    color: var(--sign-white);
    font-weight: 800;
    font-size: 56px;
    letter-spacing: 0.5em;
    margin-right: -0.5em;
    line-height: 1;
  }
  .sign__art { position: absolute; }
  .sign__art--violin {
    left: 0; top: 72px; width: 128px; height: 324px;
    background: radial-gradient(ellipse at 50% 65%, rgba(90,90,90,.35), rgba(160,160,160,.12) 60%, transparent 75%);
  }
  .sign__art--clef {
    left: 950px; top: 78px; width: 106px; height: 318px;
    background: radial-gradient(ellipse at 50% 50%, rgba(40,40,40,.6), rgba(90,90,90,.25) 55%, transparent 75%);
  }
  .sign__name {
    position: absolute; left: 0; right: 0; top: 94px;
    text-align: center;
    font-weight: 800;
    font-size: 64px;
    line-height: 1.15;
    color: var(--headline-red);
  }
  .sign__lessons-es {
    position: absolute; left: 0; right: 0; top: 266px;
    text-align: center;
    font-weight: 700;
    font-size: 22.5px;
    color: var(--ink);
  }
  .sign__lessons-en {
    position: absolute; left: 0; right: 0; top: 295px;
    text-align: center;
    font-weight: 800;
    font-size: 41px;
    line-height: 1.05;
    color: var(--headline-red);
  }
  .sign__contact {
    position: absolute; left: 0; right: 0; top: 352px;
    display: flex; justify-content: center; align-items: center; gap: 14px;
    font-weight: 700;
    font-size: 25px;
    color: var(--ink-soft);
  }
  .contact-item { display: flex; align-items: center; gap: 10px; }
  .contact-icon { width: 22px; height: 22px; flex: none; }
  .caption {
    position: absolute; left: 0; right: 0; top: 528px;
    text-align: center;
    color: var(--caption);
    font-weight: 600;
    font-size: 30px;
  }
</style>
</head>
<body>
  <section class="sign">
    <header class="sign__band"><h1 class="sign__band-title">MUSIC ACADEMY</h1></header>

    <div class="sign__art sign__art--violin" role="img" aria-label="Violin silhouette built from scattered music notes"></div>
    <div class="sign__art sign__art--clef" role="img" aria-label="Treble clef drawn with piano keys"></div>

    <h2 class="sign__name">THE RANCHERA LOFT<br>OF DELANO</h2>

    <p class="sign__lessons-es">LECCIONES DE PIANO, VIOLIN, GUITARRA, VOZ, TROMPETA Y MAS</p>
    <p class="sign__lessons-en">GUITAR, VOICE, TRUMPET AND MORE</p>

    <div class="sign__contact">
      <span class="contact-item">
        <svg class="contact-icon" viewBox="0 0 24 24" aria-hidden="true">
          <circle cx="12" cy="12" r="12" fill="var(--headline-red)"/>
          <path d="M9 6.5c.5-.3 1-.2 1.3.3l1 1.8c.2.4.1.9-.3 1.2l-.8.6c.4 1.4 1.3 2.6 2.6 3.3l.6-.8c.3-.4.8-.5 1.2-.3l1.8 1c.5.3.6.8.3 1.3l-.7 1c-.4.6-1.2.9-1.9.6-3-1.2-5.2-3.7-6.1-6.8-.2-.7.1-1.4.7-1.8z" fill="#fff"/>
        </svg>
        (661) 555-0147
      </span>
      <span class="contact-item">
        <svg class="contact-icon" viewBox="0 0 24 24" aria-hidden="true">
          <circle cx="12" cy="12" r="10.5" fill="none" stroke="var(--headline-red)" stroke-width="2"/>
          <ellipse cx="12" cy="12" rx="4.5" ry="10.5" fill="none" stroke="var(--headline-red)" stroke-width="1.8"/>
          <path d="M1.5 12h21M3.5 7h17M3.5 17h17" stroke="var(--headline-red)" stroke-width="1.6"/>
        </svg>
        WWW.THERANCHERALOFT.EXAMPLE
      </span>
    </div>
  </section>

  <p class="caption">8X3 FRONT LIT SIGN</p>
</body>
</html>
```